Web tool bar Project

I'm open to paying more if the quality of the bar is very good... if you feel the scope of the project does not match budget..... please quote me.

I need someone to re-design my web tool bar.

In the first attachment you can see a black tool bar (fig1). This is my old design. I want this to be the template as it shows what the text will say and where the buttons will be placed.

For the new tool bar:
-I would like the it to be white in colour (like fig.2)
-I would like the buttons to also be white. But the buttons must stand out so the designer should use the right shading to make the buttons stand out.
-The bar needs to be the quality of the bar in fig.2 (very good quality). I have had many designs done for this but no designer seems to be good enough to get the right quality.
-The text in the white boxes on the new bar should be the colours shown above the buttons next to fig.1 (blue, green, red, yellow, purple & orange).

Finally please put the logo attached (QT) at the end of the bar on the right where it says logo. The logo should blend in well with the bar as it has white in it also.

Please take note of fig.2 it is good quality with sharp edges I would like the same quality.

Any further questions please ask?

Requirements
Must have
• Quality!

```html
<!DOCTYPE html>
<html lang="en">
<head>
<meta charset="utf-8">
<title>Web Toolbar</title>
<link rel="stylesheet" href="https://fonts.googleapis.com/css2?family=Roboto+Condensed:wght@700&display=swap">
<style>
  :root {
    --page-bg: #ffffff;
    --stage-dark: #000000;
    --bar-top: #fbfbfb;
    --bar-bottom: #dedede;
    --bar-edge: #c9c9c9;
    --btn-top: #ffffff;
    --btn-bottom: #e4e4e4;
    --btn-edge: #bdbdbd;
    --divider: #c4c4c4;
    --green: #5cd11e;
    --red: #d3131b;
    --yellow: #f0c11c;
    --purple: #c01cb6;
    --orange: #f4861c;
    --brand-blue: #1a9be0;
  }
  * { box-sizing: border-box; margin: 0; padding: 0; }
  html, body {
    width: 1200px; height: 165px; overflow: hidden;
    background: var(--page-bg);
    font-family: "Roboto Condensed", "Arial Narrow", sans-serif;
  }
  .canvas { position: relative; width: 1200px; height: 165px; }
  .stage-dark {
    position: absolute; left: 0; top: 0; width: 1200px; height: 80px;
    background: var(--stage-dark);
  }
  .toolbar {
    position: absolute; left: 20px; width: 1160px; height: 42px;
    background: linear-gradient(to bottom, var(--bar-top), var(--bar-bottom));
    border: 1px solid var(--bar-edge);
  }
  .toolbar--dark-stage { top: 19px; }
  .toolbar--light-stage { top: 98px; }

  .btn {
    position: absolute; top: 6px; height: 28px;
    display: flex; align-items: center; justify-content: center; gap: 5px;
    background: linear-gradient(to bottom, var(--btn-top), var(--btn-bottom));
    border: 1px solid var(--btn-edge);
    border-radius: 3px;
    box-shadow: 0 1px 1px rgba(0,0,0,0.12), inset 0 1px 0 #fff;
    font-size: 10px; font-weight: 700; white-space: nowrap; overflow: hidden;
  }
  .btn svg { flex: none; }
  .btn-group { left: 601px; width: 185px; justify-content: flex-start; gap: 0; }
  .btn-group .segment { flex: none; display: flex; align-items: center; gap: 3px; height: 100%; }
  .btn-group .divider { flex: none; width: 1px; height: 20px; background: var(--divider); }
  .segment--checkin { color: var(--green); width: 60px; padding-left: 4px; }
  .segment--friends { color: var(--red); padding-left: 8px; gap: 5px; }
  .btn-feeds { left: 794px; width: 93px; color: var(--yellow); }
  .btn-messages { left: 895px; width: 80px; color: var(--purple); }
  .btn-scrapbook { left: 982px; width: 80px; color: var(--orange); }

  .brand {
    position: absolute; left: 1098px; top: 7px; height: 28px;
    display: flex; align-items: center; gap: 4px;
    color: var(--brand-blue); font-size: 16px; font-weight: 700;
  }
  .brand-square { width: 10px; height: 10px; background: var(--brand-blue); }
</style>
</head>
<body>
<div class="canvas">
  <div class="stage-dark"></div>

  <nav class="toolbar toolbar--dark-stage" aria-label="Site toolbar on dark background">
    <div class="btn btn-group">
      <span class="segment segment--checkin">
        <svg width="11" height="11" viewBox="0 0 11 11"><rect x="0.5" y="1.5" width="9" height="9" fill="none" stroke="currentColor"/><path d="M2.5 5.5 L5 8 L10.5 1" fill="none" stroke="currentColor" stroke-width="1.6"/></svg>
        Check - In
      </span>
      <span class="divider"></span>
      <span class="segment segment--friends">
        <svg width="10" height="11" viewBox="0 0 10 11"><circle cx="5" cy="3" r="2.6" fill="currentColor"/><rect x="0.5" y="6.2" width="9" height="4.8" rx="1" fill="currentColor"/></svg>
        Online Fiends at Gather+
      </span>
    </div>
    <div class="btn btn-feeds">
      <svg width="12" height="12" viewBox="0 0 11 11"><circle cx="1.6" cy="9.4" r="1.6" fill="currentColor"/><path d="M0 4.8 A6.2 6.2 0 0 1 6.2 11" fill="none" stroke="currentColor" stroke-width="1.7"/><path d="M0 0.9 A10.1 10.1 0 0 1 10.1 11" fill="none" stroke="currentColor" stroke-width="1.7"/></svg>
      Lounge Feeds
    </div>
    <div class="btn btn-messages">
      <svg width="13" height="10" viewBox="0 0 13 10"><rect width="13" height="10" rx="1" fill="currentColor"/><path d="M0.5 1 L6.5 5.5 L12.5 1" fill="none" stroke="#fff" stroke-width="1"/></svg>
      Messages
    </div>
    <div class="btn btn-scrapbook">
      <svg width="13" height="11" viewBox="0 0 13 11"><path d="M2 1 H12 L11 8 H1 Z" fill="currentColor"/><path d="M1 8 H11 L10.6 10.5 H0.6 Z" fill="#f9c27f"/></svg>
      Scrapbook
    </div>
    <div class="brand"><span class="brand-square"></span>QT</div>
  </nav>

  <nav class="toolbar toolbar--light-stage" aria-label="Site toolbar on light background">
    <div class="btn btn-group">
      <span class="segment segment--checkin">
        <svg width="11" height="11" viewBox="0 0 11 11"><rect x="0.5" y="1.5" width="9" height="9" fill="none" stroke="currentColor"/><path d="M2.5 5.5 L5 8 L10.5 1" fill="none" stroke="currentColor" stroke-width="1.6"/></svg>
        Check - In
      </span>
      <span class="divider"></span>
      <span class="segment segment--friends">
        <svg width="10" height="11" viewBox="0 0 10 11"><circle cx="5" cy="3" r="2.6" fill="currentColor"/><rect x="0.5" y="6.2" width="9" height="4.8" rx="1" fill="currentColor"/></svg>
        Online Fiends at Gather+
      </span>
    </div>
    <div class="btn btn-feeds">
      <svg width="12" height="12" viewBox="0 0 11 11"><circle cx="1.6" cy="9.4" r="1.6" fill="currentColor"/><path d="M0 4.8 A6.2 6.2 0 0 1 6.2 11" fill="none" stroke="currentColor" stroke-width="1.7"/><path d="M0 0.9 A10.1 10.1 0 0 1 10.1 11" fill="none" stroke="currentColor" stroke-width="1.7"/></svg>
      Lounge Feeds
    </div>
    <div class="btn btn-messages">
      <svg width="13" height="10" viewBox="0 0 13 10"><rect width="13" height="10" rx="1" fill="currentColor"/><path d="M0.5 1 L6.5 5.5 L12.5 1" fill="none" stroke="#fff" stroke-width="1"/></svg>
      Messages
    </div>
    <div class="btn btn-scrapbook">
      <svg width="13" height="11" viewBox="0 0 13 11"><path d="M2 1 H12 L11 8 H1 Z" fill="currentColor"/><path d="M1 8 H11 L10.6 10.5 H0.6 Z" fill="#f9c27f"/></svg>
      Scrapbook
    </div>
    <div class="brand"><span class="brand-square"></span>QT</div>
  </nav>
</div>
</body>
</html>
```